Stationery Design Project - Ma clairiere

We are a french company, Ma Clairiere. It means My Glade.
We own and manage woods, we transform it industrially into very high quality (dry) logs and pellets and we commercialize them to individuals in France.
People can order the logs online or by phone and get the wood logs delivered at home.

After our great logo contest, we would like to launch a new stationery project.
Updates

Target Market(s)

inhabitants of sub-urban areas in France. (living in houses not in apartment )

Industry/Entity Type

It Company

Requirements
Must have
• content see attachment
logo

For the business card, we would like on the front side, the logo, name + contact info. We would like to use the back side for commercial purpose insisting on our distinctive value proposition.
Nice to have
• the back side of the business card can be more colorful

```html
<!DOCTYPE html>
<html lang="fr">
<head>
<meta charset="utf-8">
<title>Ma Clairiere – Cartes de visite</title>
<link rel="stylesheet" href="https://fonts.googleapis.com/css2?family=Montserrat:wght@400;500;700;800&display=swap">
<style>
  :root {
    --bg: #2b2b2d;
    --navy-light: #1d4a63;
    --navy: #123246;
    --navy-deep: #0b2233;
    --red: #d3233a;
    --white: #ffffff;
    --text-soft: #e8eef2;
    --wood: #c9a57e;
    --shirt: #b0262f;
  }
  * { box-sizing: border-box; margin: 0; padding: 0; }
  html, body { width: 1200px; height: 901px; overflow: hidden; }
  body {
    background: var(--bg);
    font-family: "Montserrat", sans-serif;
    display: flex;
    align-items: center;
    justify-content: center;
    gap: 70px;
  }
  .card {
    position: relative;
    width: 360px;
    height: 560px;
    border-radius: 26px;
    overflow: hidden;
    background: radial-gradient(ellipse at 40% 30%, var(--navy-light) 0%, var(--navy) 55%, var(--navy-deep) 100%);
    box-shadow: 0 20px 40px rgba(0,0,0,.45);
    color: var(--text-soft);
  }

  /* ---------- back side: value proposition ---------- */
  .back .brand-vertical {
    position: absolute;
    left: 40px;
    top: 40px;
    height: 480px;
    writing-mode: vertical-rl;
    transform: rotate(180deg);
    font-weight: 800;
    font-size: 74px;
    letter-spacing: -2px;
    color: var(--red);
    line-height: 1;
    text-align: center;
    white-space: nowrap;
  }
  .back .mascot {
    position: absolute;
    left: 165px;
    top: 40px;
    width: 150px;
    height: 240px;
    border-radius: 14px;
    background: linear-gradient(180deg, var(--wood) 0%, var(--shirt) 40%, var(--navy-light) 75%, var(--navy) 100%);
    opacity: .85;
  }
  .back .pitch {
    position: absolute;
    left: 160px;
    top: 305px;
    width: 175px;
    font-size: 12.5px;
    line-height: 1.35;
    color: var(--white);
  }
  .back .pitch p + p { margin-top: 14px; }

  /* ---------- front side: contact ---------- */
  .front .brand {
    position: absolute;
    left: 32px;
    top: 60px;
    font-weight: 800;
    font-size: 38px;
    letter-spacing: -1px;
    color: var(--white);
  }
  .front .contact {
    position: absolute;
    left: 0;
    right: 0;
    top: 125px;
    text-align: center;
  }
  .front .person {
    font-size: 17px;
    font-weight: 500;
    color: var(--white);
    margin-bottom: 14px;
  }
  .front .person .surname { color: var(--red); }
  .front .label {
    font-size: 9px;
    color: var(--red);
    line-height: 1.2;
  }
  .front .value {
    font-size: 16px;
    font-weight: 500;
    color: var(--white);
    line-height: 1.3;
    margin-bottom: 6px;
  }
  .front .mascot {
    position: absolute;
    left: 60px;
    bottom: 0;
    width: 260px;
    height: 200px;
    border-radius: 40px 40px 0 0;
    background: linear-gradient(180deg, var(--wood) 0%, var(--shirt) 55%, var(--navy-deep) 100%);
    opacity: .85;
  }
</style>
</head>
<body>

  <section class="card back" aria-label="Verso de la carte">
    <div class="brand-vertical">Ma Clairiere</div>
    <div class="mascot" role="img" aria-label="Illustration d'un bûcheron en chemise à carreaux portant un plateau de bûches"></div>
    <div class="pitch">
      <p>Livraison gratuite de bois de chauffage à Lyon et région. Bûches, granulés, briquettes</p>
      <p>Commandez sur www.maclairiere.fr ou au 04 72 18 40 26</p>
      <p>Qualité supérieure, origine France certifiée</p>
    </div>
  </section>

  <section class="card front" aria-label="Recto de la carte">
    <div class="brand">Ma Clairiere</div>
    <div class="contact">
      <p class="person">Étienne <span class="surname">MARCHAND</span></p>
      <p class="label">Tel</p>
      <p class="value">04 72 18 40 26</p>
      <p class="label">Mobile</p>
      <p class="value">04 72 18 40 26</p>
      <p class="label">Email</p>
      <p class="value">marchand@maclairiere.fr</p>
      <p class="label">Site web</p>
      <p class="value">www.maclairiere.fr</p>
    </div>
    <div class="mascot" role="img" aria-label="Illustration d'un bûcheron tenant un plateau de bûches"></div>
  </section>

</body>
</html>
```